real esate business card with company logo and name

we need a business card design for a real esate company

The company name is Walsh & Brody Pty Ltd, and we have our logo designed and will upload. We want classic or moden feel. Black or white background. looks more textured. Should include folowinginformations
Paul Walsh and Lucy Brody
Sales Agents & Onsite Manager
p: 07 5948 2063
F: 07 5948 2174
M:0461 857 239
3/42 Marlin Crescent, ELLEN GROVE QLD 4078

We want this business card looks professonal. Thank you in advance.

Industry/Entity Type

Real Estate Agent

Contact Information for Business Card

Paul Walsh and Lucy Brody
Onsite Manager & Sales Agents
p: 07 5948 2063
M:0461 857 239

Font styles to use
Serif

Colors
000000
fbfbfb
333333
959595

Requirements
Must have
• company logo and name, black or white back ground

```html
<!DOCTYPE html>
<html lang="en">
<head>
<meta charset="utf-8">
<title>Walsh &amp; Brody Pty Ltd — Business Card</title>
<link rel="stylesheet" href="https://fonts.googleapis.com/css2?family=Nunito+Sans:wght@400;600;800&display=swap">
<style>
  :root {
    --page-bg: #e4e4e4;
    --card-bg: #fbfbfb;
    --card-edge: #959595;
    --ink-strong: #000000;
    --ink: #333333;
    --ink-soft: #555555;
    --mark: #7a7a7a;
  }
  * { margin: 0; padding: 0; box-sizing: border-box; }
  html, body {
    width: 1200px;
    height: 970px;
    overflow: hidden;
    background: var(--page-bg);
    font-family: "Nunito Sans", "Helvetica Neue", Arial, sans-serif;
  }
  .canvas {
    position: relative;
    width: 1200px;
    height: 970px;
  }
  .card {
    position: absolute;
    left: 100px;
    top: 207px;
    width: 1000px;
    height: 556px;
    background: var(--card-bg);
    border: 1px solid var(--card-edge);
    box-shadow: 0 10px 30px rgba(0,0,0,0.12);
  }
  .brand {
    position: absolute;
    left: 110px;
    top: 118px;
    width: 300px;
    display: flex;
    flex-direction: column;
    align-items: center;
  }
  .brand-square {
    width: 190px;
    height: 190px;
    background: var(--mark);
  }
  .brand-name {
    margin-top: 56px;
    font-size: 27px;
    font-weight: 600;
    letter-spacing: 0.5px;
    color: var(--ink);
    text-transform: uppercase;
    white-space: nowrap;
  }
  .details {
    position: absolute;
    left: 553px;
    top: 143px;
    color: var(--ink);
  }
  .agents {
    font-size: 28px;
    font-weight: 800;
    color: var(--ink-strong);
    letter-spacing: 0.6px;
    text-transform: uppercase;
    white-space: nowrap;
  }
  .agents .divider { font-weight: 400; margin: 0 10px; }
  .role {
    font-size: 23px;
    color: var(--ink-soft);
    margin-top: 2px;
  }
  .address {
    font-size: 23px;
    line-height: 34px;
    margin-top: 34px;
    font-style: normal;
    color: var(--ink-soft);
  }
  .contacts {
    list-style: none;
    margin-top: 20px;
  }
  .contacts li {
    display: flex;
    align-items: center;
    font-size: 23px;
    line-height: 36px;
    color: var(--ink-soft);
  }
  .contacts svg {
    width: 20px;
    height: 20px;
    margin-right: 14px;
    fill: var(--ink);
  }
</style>
</head>
<body>
<main class="canvas">
  <section class="card">
    <div class="brand">
      <div class="brand-square" aria-hidden="true"></div>
      <p class="brand-name">Walsh &amp; Brody Pty Ltd.</p>
    </div>

    <div class="details">
      <h1 class="agents">Paul Walsh<span class="divider">|</span>Lucy Brody</h1>
      <p class="role">Onsite Manager &amp; Sales Agents</p>

      <address class="address">
        3/42 Marlin Crescent,<br>
        ASHVALE PARK QLD 4519
      </address>

      <ul class="contacts">
        <li>
          <svg viewBox="0 0 20 20" aria-label="Mobile"><path d="M6 1h8a1.5 1.5 0 0 1 1.5 1.5v15A1.5 1.5 0 0 1 14 19H6a1.5 1.5 0 0 1-1.5-1.5v-15A1.5 1.5 0 0 1 6 1zm0.3 2v12.5h7.4V3zM10 16.3a0.9 0.9 0 1 0 0 1.8a0.9 0.9 0 0 0 0-1.8z" fill-rule="evenodd"/></svg>
          0461 857 239
        </li>
        <li>
          <svg viewBox="0 0 20 20" aria-label="Phone"><path d="M2 6.5C2 4.5 5.5 3 10 3s8 1.5 8 3.5v1.5h-4V6.3c-1-.4-2.4-.6-4-.6s-3 .2-4 .6V8H2zM5 9h10l2 8H3zm5 2.2a2.3 2.3 0 1 0 0 4.6a2.3 2.3 0 0 0 0-4.6z" fill-rule="evenodd"/></svg>
          07 5948 2063
        </li>
        <li>
          <svg viewBox="0 0 20 20" aria-label="Fax"><path d="M5 2h10v4H5zM2 7h16v8h-3v-3H5v3H2zM6 13h8v5H6z"/></svg>
          07 5948 2174
        </li>
      </ul>
    </div>
  </section>
</main>
</body>
</html>
```